Modern Email Signature & Alert Email Template

We are a car leasing company and are looking for a revamp to our emails. We would like a more modern & sleek presentation when we are emailing our clients. We would like a signature for our employees & a general template for notifications e.g. Lease Ending.

Would like to be able to copy & paste the email formatting to outlook & to our notification sending system.

Attached is our logo & the alert email that we send out.

Industry/Entity Type

Car Leasing

Colors

Designer to choose colors to be used in the design.

Requirements
Must have
• Our logo & Contact information

```html
<!DOCTYPE html>
<html lang="en">
<head>
<meta charset="utf-8">
<title>Brisk Auto Leasing – Email Signature</title>
<link rel="stylesheet" href="https://fonts.googleapis.com/css2?family=Arimo:wght@400;700&display=swap">
<style>
  :root {
    --backdrop: #b2b2b2;
    --card: #ffffff;
    --brand-blue: #0a5ad4;
    --band-light: #00a0e9;
    --band-dark: #0040c0;
    --steel-light: #d6d6d6;
    --steel-dark: #6e6e6e;
    --text-grey: #5f5f5f;
    --rule: #8a8a8a;
  }
  * { box-sizing: border-box; margin: 0; padding: 0; }
  html, body {
    width: 1200px; height: 1200px; overflow: hidden;
    background: var(--backdrop);
    font-family: "Arimo", Arial, sans-serif;
  }
  .signature {
    position: absolute; left: 110px; top: 375px;
    width: 980px; height: 450px;
    background: var(--card);
    box-shadow: 4px 5px 6px rgba(0,0,0,0.3);
    overflow: hidden;
  }
  .signature__header { position: absolute; left: 0; top: 0; width: 980px; height: 140px; }
  .brand-name {
    position: absolute; left: 68px; top: 160px;
    font-weight: 700; font-size: 46px; letter-spacing: 1px;
    color: var(--brand-blue); white-space: nowrap;
  }
  .person {
    position: absolute; left: 70px; top: 268px;
    font-size: 34px; white-space: nowrap; line-height: 1;
  }
  .person__name { font-weight: 700; color: var(--brand-blue); }
  .person__divider { font-weight: 700; color: var(--band-light); margin: 0 6px; }
  .person__role { color: var(--text-grey); font-size: 31px; }
  .contacts {
    position: absolute; left: 70px; top: 330px; width: 705px;
    display: flex; align-items: center; justify-content: space-between;
    font-size: 28px; color: var(--text-grey); line-height: 1;
    padding-bottom: 9px; border-bottom: 2px solid var(--rule);
  }
  .contacts__item { display: flex; align-items: center; gap: 10px; white-space: nowrap; }
  .contacts__icon { width: 24px; height: 24px; fill: none; stroke: var(--brand-blue); stroke-width: 2; }
  .address {
    position: absolute; left: 70px; top: 381px;
    font-size: 23px; color: var(--text-grey); white-space: nowrap;
  }
</style>
</head>
<body>
  <div class="signature">
    <svg class="signature__header" viewBox="0 0 980 140" aria-hidden="true">
      <defs>
        <linearGradient id="band" x1="0" x2="1" y1="0" y2="0">
          <stop offset="0" stop-color="var(--band-light)"/>
          <stop offset="1" stop-color="var(--band-dark)"/>
        </linearGradient>
        <linearGradient id="steel" x1="0" x2="0" y1="0" y2="1">
          <stop offset="0" stop-color="var(--steel-dark)"/>
          <stop offset="0.5" stop-color="var(--steel-light)"/>
          <stop offset="1" stop-color="var(--steel-dark)"/>
        </linearGradient>
        <linearGradient id="swoosh" x1="0" x2="1">
          <stop offset="0" stop-color="var(--steel-dark)"/>
          <stop offset="1" stop-color="var(--steel-light)"/>
        </linearGradient>
      </defs>
      <path d="M0 0 H980 V119 H540 C380 119 300 60 230 80 C150 100 70 60 0 12 Z" fill="url(#band)"/>
      <path d="M0 12 C70 60 130 82 230 80 C140 96 60 78 0 56 Z" fill="url(#swoosh)"/>
      <rect x="536" y="120" width="444" height="13" fill="url(#steel)"/>
    </svg>

    <div class="brand-name">BRISK AUTO LEASING</div>

    <div class="person">
      <span class="person__name">DANIEL HAYES</span><span class="person__divider">|</span><span class="person__role">Manager</span>
    </div>

    <div class="contacts">
      <span class="contacts__item">
        <svg class="contacts__icon" viewBox="0 0 24 24"><path d="M5 3 L9 3 L10 8 L7.5 9.5 C8.5 12 11 14.5 14 16 L15.5 13.5 L20.5 14.5 L20.5 19 C12 20 4 12 5 3 Z"/><path d="M14 4 A6 6 0 0 1 20 10 M14 7 A3 3 0 0 1 17 10"/></svg>
        345-555-0148
      </span>
      <span class="contacts__item">
        <svg class="contacts__icon" viewBox="0 0 24 24"><rect x="3" y="5.5" width="18" height="13" rx="1.5"/><path d="M3.5 6.5 L12 13 L20.5 6.5"/></svg>
        service@briskauto.ky
      </span>
      <span class="contacts__item">
        <svg class="contacts__icon" viewBox="0 0 24 24"><circle cx="12" cy="12" r="9"/><ellipse cx="12" cy="12" rx="4" ry="9"/><path d="M3 12 H21 M4.5 7.5 H19.5 M4.5 16.5 H19.5"/></svg>
        www.briskauto.ky
      </span>
    </div>

    <div class="address">P.O Box 582, Grand Cayman KY1-1208, CAYMAN ISLANDS</div>
  </div>
</body>
</html>
```